KVO-Business Card Design

I need a modern, professional business card design that includes my logo as the main feature, maybe the entire background with the contact info overlaying or even contact info on the back and the logo full frontal

Neat and organized placement of contact information

Would like to see options in black and white

Target Market(s)

real estate Developers, Construction managers, business and home owners

Industry/Entity Type

Construction

Contact Information for Business Card

KVO Construction
Danny Ferrante
General Contractor

Office: 1-888-902-7315 Ext #1
Cell: 215-730-4162
Fax: 1-888-902-7315

Font styles to use
Serif

Requirements
Must have
• title
• office #
• cell #
• Email
• website
Nice to have
• fax

```html
<!DOCTYPE html>
<html lang="en">
<head>
<meta charset="utf-8">
<title>KVO Construction – Business Card</title>
<link rel="stylesheet" href="https://fonts.googleapis.com/css2?family=Arimo:wght@400;700&display=swap">
<style>
  :root{
    --bg:#8c8d8f;
    --card-white:#f4f4f4;
    --green-dark:#1c6a2e;
    --green-mid:#2f8a3a;
    --green-light:#7dbb3c;
    --green-deep:#0c5430;
    --grey-text:#4a4c50;
    --grey-rule:#6a6c70;
    --grey-band:#66686c;
  }
  *{box-sizing:border-box;margin:0;padding:0}
  html,body{width:1105px;height:1200px;overflow:hidden}
  body{background:var(--bg);font-family:"Arimo",Arial,sans-serif;position:relative}

  .card{position:absolute;left:180px;width:746px;height:427px;overflow:hidden}

  /* front */
  .card-front{top:118px;background:var(--card-white)}
  .brand-name{position:absolute;right:58px;top:104px;font-weight:700;font-size:40px;color:var(--green-dark);letter-spacing:1px}
  .side-tab{position:absolute;left:0;top:261px;width:8px;height:51px;background:var(--grey-band)}
  .person-name{position:absolute;left:43px;top:260px;font-size:25px;font-weight:700;color:var(--green-dark)}
  .person-title{position:absolute;left:43px;top:290px;font-size:17px;color:var(--grey-text)}
  .title-rule{position:absolute;left:43px;right:56px;top:310px;height:2px;background:var(--grey-rule)}
  .contact{position:absolute;display:flex;flex-direction:column;gap:9px;font-size:19px;color:var(--grey-text)}
  .contact-left{left:43px;top:330px}
  .contact-right{left:498px;top:330px;font-size:18px}
  .contact-row{display:flex;align-items:center;gap:11px;height:20px}
  .contact-row svg{width:15px;height:17px;fill:var(--green-dark);flex:none}
  .bottom-band{position:absolute;left:0;right:0;bottom:0;height:17px}

  /* back */
  .card-back{top:636px;background:radial-gradient(ellipse 55% 75% at 50% 35%,var(--green-light) 0%,var(--green-mid) 45%,var(--green-deep) 100%)}
  .back-brand{position:absolute;left:0;right:0;top:170px;text-align:center;font-weight:700;font-size:56px;color:#fff;letter-spacing:2px}
  .website{position:absolute;left:0;right:0;top:352px;text-align:center;font-size:19px;color:#fff;letter-spacing:4.3px}
</style>
</head>
<body>

<section class="card card-front">
  <div class="brand-name">KVO Construction</div>
  <div class="side-tab"></div>
  <h1 class="person-name">Danny Ferrante</h1>
  <p class="person-title">General Contractor</p>
  <div class="title-rule"></div>

  <div class="contact contact-left">
    <div class="contact-row">
      <svg viewBox="0 0 24 24"><path d="M6.6 10.8a15.2 15.2 0 0 0 6.6 6.6l2.2-2.2a1 1 0 0 1 1-.25 11.4 11.4 0 0 0 3.6.57 1 1 0 0 1 1 1V20a1 1 0 0 1-1 1A17 17 0 0 1 3 4a1 1 0 0 1 1-1h3.5a1 1 0 0 1 1 1c0 1.25.2 2.45.57 3.57a1 1 0 0 1-.25 1z"/></svg>
      <span>1-888-902-7315 Ext #1</span>
    </div>
    <div class="contact-row">
      <svg viewBox="0 0 24 24"><path d="M7 1h10a2 2 0 0 1 2 2v18a2 2 0 0 1-2 2H7a2 2 0 0 1-2-2V3a2 2 0 0 1 2-2zm0 3v15h10V4z"/></svg>
      <span>215-730-4162</span>
    </div>
  </div>

  <div class="contact contact-right">
    <div class="contact-row">
      <svg viewBox="0 0 24 24"><path d="M6 2h10l2 2v5h1a3 3 0 0 1 3 3v7h-4v3H6v-3H2v-7a3 3 0 0 1 3-3h1zm2 2v5h8V5h-1V4zm0 11v5h8v-5z"/></svg>
      <span>1-888-902-7315</span>
    </div>
    <div class="contact-row">
      <svg viewBox="0 0 24 24"><path d="M2 5h20v14H2zm2 2v.5l8 5 8-5V7zm0 2.8V17h16V9.8l-8 5z"/></svg>
      <span>Danny@kvo.com</span>
    </div>
  </div>

  <svg class="bottom-band" viewBox="0 0 746 17" preserveAspectRatio="none">
    <defs>
      <linearGradient id="bandGreen" x1="0" x2="1">
        <stop offset="0" stop-color="#1c6a2e"/>
        <stop offset="1" stop-color="#7dbb3c"/>
      </linearGradient>
    </defs>
    <polygon points="0,0 487,0 482,17 0,17" fill="url(#bandGreen)"/>
    <polygon points="494,0 746,0 746,17 489,17" fill="#66686c"/>
  </svg>
</section>

<section class="card card-back">
  <div class="back-brand">KVO Construction</div>
  <p class="website">www.kvoconstruction.com</p>
</section>

</body>
</html>
```